Letterhead Design Project

Consulting Company , we want a letterhead incorporating both the picture provided and the logo provided. The font name is monotype corsiva.
Target Market(s)
Dentist
Industry/Entity Type
Consulting
Font styles to use
Other font styles liked:
- monotype corsiva

Colors
0455a3
Requirements
Must have
- the logo, the picture (see attached), the website name, the email. and the phone numbers.
- Website: www.tkregulatoryadvisors.solutions
- Email: will be provided to the winner, please use placeholder
- Phone numbers:
- Rhea Lindqvist 5824417093
- Omar Kettering 6148072356

Nice to have
- a swoop or wave across the bottom. a line up the side. I don't know guys. design something unique and professional.

Should not have
- arrows pointing off the logo or anywhere. no arrows. our logo altered in anyway. no broken circles. no variences in blue. we like our logo the way it is. the font is monotype corsiva

```html
<!DOCTYPE html>
<html lang="en">
<head>
<meta charset="utf-8">
<title>TK Regulatory Advisors, LLC — Letterhead</title>
<link href="https://fonts.googleapis.com/css2?family=Cormorant+Garamond:ital,wght@1,500&family=Open+Sans:wght@400;600&display=swap" rel="stylesheet">
<style>
  :root {
    --brand-blue: #0455a3;
    --wave-mid: #1a7fd0;
    --wave-light: #5fb0ea;
    --paper: #ffffff;
    --ink-grey: #5a5f66;
    --photo-dark: #3a3d42;
    --photo-light: #c9ccd1;
  }
  * { margin: 0; padding: 0; box-sizing: border-box; }
  html, body { width: 966px; height: 1200px; overflow: hidden; background: var(--paper); }
  .letterhead { position: relative; width: 966px; height: 1200px; background: var(--paper); overflow: hidden; }

  .brand { position: absolute; left: 46px; top: 40px; display: flex; align-items: center; gap: 18px; }
  .brand-dot { width: 84px; height: 84px; border-radius: 50%; border: 3px solid var(--brand-blue); flex: none; }
  .brand-text { display: flex; flex-direction: column; }
  .brand-name {
    font-family: "Cormorant Garamond", serif; font-style: italic; font-weight: 500;
    font-size: 40px; color: var(--brand-blue); line-height: 1;
  }
  .brand-address {
    margin-top: 6px; font-family: "Open Sans", sans-serif; font-size: 11px;
    letter-spacing: 0.6px; color: var(--ink-grey); text-transform: uppercase;
  }

  .footer-waves { position: absolute; left: 0; bottom: 0; width: 966px; height: 300px; }

  .portrait {
    position: absolute; left: 740px; top: 900px; width: 190px; height: 190px; border-radius: 50%;
    border: 5px solid var(--paper);
    background: radial-gradient(circle at 50% 40%, var(--photo-light) 0%, #8d9096 55%, var(--photo-dark) 100%);
  }

  .contact {
    position: absolute; right: 38px; top: 1100px; text-align: right;
    font-family: "Open Sans", sans-serif; font-size: 13px; line-height: 20px; color: var(--paper);
  }
</style>
</head>
<body>
<main class="letterhead">
  <header class="brand">
    <div class="brand-dot"></div>
    <div class="brand-text">
      <span class="brand-name">TK Regulatory Advisors, LLC</span>
      <span class="brand-address">215 Harlow Lane, Ashford Hills, Kentucky 40987</span>
    </div>
  </header>

  <svg class="footer-waves" viewBox="0 0 966 300" aria-hidden="true">
    <path d="M0 250 C 260 270, 520 170, 966 60 L966 300 L0 300 Z" fill="var(--wave-light)" opacity="0.55"/>
    <path d="M0 270 C 300 290, 560 190, 966 100 L966 300 L0 300 Z" fill="var(--wave-mid)"/>
    <path d="M0 240 C 200 250, 420 230, 966 120" fill="none" stroke="var(--wave-light)" stroke-width="6"/>
    <path d="M0 285 C 320 300, 600 220, 966 150 L966 300 L0 300 Z" fill="var(--brand-blue)"/>
    <path d="M40 278 C 330 300, 600 210, 966 135" fill="none" stroke="var(--paper)" stroke-width="4"/>
  </svg>

  <div class="portrait" role="img" aria-label="Portrait photograph of the company consultant"></div>

  <address class="contact">
    <div>Rhea Lindqvist : 5824417093</div>
    <div>Omar Kettering : 6148072356</div>
    <div>info@tkregulatoryadvisors.solutions</div>
    <div>www.tkregulatoryadvisors.solutions</div>
  </address>
</main>
</body>
</html>
```